New Zealand Manuka Honey information banner

We are a Manuka honey export company and we are looking for a banner to show the benefits of our honey at trade shows.
Manuka honey and raw honey has a lot of health benefits and we would love you to open the creative beast inside you so that no one can walk passed our stand without stopping to read and purchase our products.
I have attached the shape of what it has to look like.
Full bleed size (artwork size)

850mm x 2060mm (10mm top and 50mm bottom)
10mm at the top for clamping purpose
50mm at the bottom to be attached to the spring machanism
Actual/Trim size (final size after mounting)
850mm x 2000mm
Note: Safe margin is 5mm from all edges (trim size)
Our role is to inform people what the benefits are of manuka honey and what the ratings mean between KRF, MGO and NPA

Target Market(s)

Health minded people

Industry/Entity Type

Health And Wellness

Font styles to use
Serif

Requirements
Must have
• Company name.. Kestrel Apiary NZ
• website... www.kestrelapiarynz.com
• Contact details kestrelapiarynz@postvale.com
• https://fx.qv/K83Tq17mzb
• There are two main components of Manuka honey which give it many health benefits:
• Hydrogen peroxide, a naturally antibiotic found in Manuka honey.
• Methylglyoxal (MG). A powerful antibiotic compound found in large quantities in Manuka honey.
• What is MGO?
• The MGO indicates the amount of Methylglyoxal in the honey. The higher the MGO rating the more antibacterial properties are in the honey.
• KRF MGO NPA
• 5+ 100+ 5
• 10+ 250+ 10
• 15+ 500+ 15
• 20+ 800+ 20
• Proven health Benefits of Active Manuka are
• Aiding in the treatment of:
• -Common Cold and Flu
• -sore throats
• -cuts and abrasions
• -Reduce hair loss and scalp problems
• -treating fungal infections
• -Burns
• -ulsers
• -strengthening the immune system
Nice to have
• Some bee related artwork in the background and something that relates our product to New Zealand
Should not have
• go crazy

```html
<!DOCTYPE html>
<html lang="en">
<head>
<meta charset="utf-8">
<title>Kestrel Apiary NZ – Manuka Honey Information Banner</title>
<link rel="stylesheet" href="https://fonts.googleapis.com/css2?family=Quicksand:wght@400;500;600&display=swap">
<style>
  :root {
    --canvas: #e6e6e4;
    --paper: #f4f4f2;
    --yellow-deep: #e3cf55;
    --yellow-mid: #ebdc74;
    --yellow-soft: #f1e7a2;
    --yellow-pale: #f6f1cf;
    --ink: #6f6a4c;
    --brand: #a39434;
    --white: #ffffff;
  }
  * { box-sizing: border-box; margin: 0; padding: 0; }
  html, body {
    width: 800px; height: 1200px; overflow: hidden;
    background: var(--canvas);
    font-family: "Quicksand", sans-serif;
    color: var(--ink);
  }
  .banner {
    position: absolute; left: 128px; top: 20px;
    width: 544px; height: 1160px;
    background: var(--paper);
    overflow: hidden;
    box-shadow: 0 2px 10px rgba(0,0,0,.12);
  }
  .banner-shapes { position: absolute; inset: 0; width: 544px; height: 1160px; }

  .contact {
    position: absolute; left: 50px; top: 52px;
    font-size: 12.5px; letter-spacing: 2px; text-transform: uppercase;
    line-height: 24px; font-weight: 500;
  }
  .brand {
    position: absolute; right: 34px; top: 62px;
    display: flex; flex-direction: column; align-items: center; gap: 6px;
  }
  .brand-dot { width: 14px; height: 14px; border-radius: 50%; background: var(--yellow-deep); }
  .brand-name { font-size: 15px; font-weight: 500; color: var(--brand); }

  .hex-text {
    position: absolute; display: flex; flex-direction: column;
    align-items: center; justify-content: center; text-align: center;
    text-transform: uppercase; font-weight: 600;
  }
  .components-title { font-size: 9.5px; line-height: 13px; letter-spacing: .5px; padding: 0 14px; }
  .component { font-size: 7.5px; line-height: 10px; padding: 0 16px; }
  .component-name { font-size: 8px; margin-bottom: 5px; }
  .component-desc { text-transform: none; font-weight: 500; }

  .benefit { font-size: 8.5px; line-height: 11px; padding: 0 16px; gap: 9px; letter-spacing: .3px; }

  .ratings-title {
    position: absolute; left: 192px; top: 902px; width: 160px;
    text-align: center; font-size: 10px; font-weight: 600;
    letter-spacing: 1px; line-height: 13px; text-transform: uppercase;
  }
  .rating-col { position: absolute; width: 50px; text-align: center; font-size: 12px; line-height: 25px; }
  .rating-col.krf { left: 165px; top: 932px; }
  .rating-col.mgo { left: 247px; top: 942px; }
  .rating-col.npa { left: 329px; top: 932px; }
  .scale-label {
    position: absolute; width: 52px; height: 30px; line-height: 30px;
    text-align: center; font-size: 17px; font-weight: 600;
  }
  .scale-label.krf { left: 164px; top: 1049px; }
  .scale-label.mgo { left: 246px; top: 1074px; }
  .scale-label.npa { left: 328px; top: 1049px; }

  .note { position: absolute; font-size: 8px; line-height: 10.5px; font-weight: 500; }
  .note.krf-note { left: 26px; top: 1084px; width: 128px; }
  .note.mgo-note { left: 122px; top: 1131px; width: 300px; text-align: center; }
  .note.npa-note { left: 392px; top: 1074px; width: 128px; }
</style>
</head>
<body>
<main class="banner">
  <svg class="banner-shapes" viewBox="0 0 544 1160" xmlns="http://www.w3.org/2000/svg">
    <defs>
      <linearGradient id="honeyPhoto" x1="0" y1="0" x2="1" y2="1">
        <stop offset="0" stop-color="#b8743a"/>
        <stop offset="0.35" stop-color="#efe6da"/>
        <stop offset="0.7" stop-color="#f7f3ee"/>
        <stop offset="1" stop-color="#d99a3a"/>
      </linearGradient>
    </defs>
    <rect class="header-band" x="0" y="0" width="544" height="140" fill="var(--yellow-pale)"/>
    <polygon class="header-accent" points="0,0 330,0 150,140 0,140" fill="var(--yellow-soft)"/>
    <rect class="photo-area" x="0" y="140" width="544" height="562" fill="url(#honeyPhoto)" role="img" aria-label="Photo of Manuka honey dripping from a dipper into a white bowl, with jars behind"/>
    <polygon class="photo-corner" points="0,140 170,140 0,330" fill="var(--yellow-mid)"/>
    <polygon class="hex components-main" points="136,430 196.6,465 196.6,535 136,570 75.4,535 75.4,465" fill="var(--yellow-soft)"/>
    <polygon class="hex component-a" points="78,550 131.7,581 131.7,643 78,674 24.3,643 24.3,581" fill="var(--yellow-pale)" opacity=".88"/>
    <polygon class="hex component-b" points="192,550 245.7,581 245.7,643 192,674 138.3,643 138.3,581" fill="var(--yellow-pale)" opacity=".88"/>
    <polygon class="hex benefit-hex" points="88,722 143.4,754 143.4,818 88,850 32.6,818 32.6,754" fill="var(--yellow-deep)"/>
    <polygon class="hex benefit-hex" points="200,722 255.4,754 255.4,818 200,850 144.6,818 144.6,754" fill="var(--yellow-mid)"/>
    <polygon class="hex benefit-hex" points="312,722 367.4,754 367.4,818 312,850 256.6,818 256.6,754" fill="var(--yellow-soft)"/>
    <polygon class="hex benefit-hex" points="424,722 479.4,754 479.4,818 424,850 368.6,818 368.6,754" fill="var(--yellow-deep)"/>
    <polygon class="footer-left" points="0,900 0,1160 320,1160" fill="var(--yellow-pale)"/>
    <polygon class="footer-right" points="544,940 544,1160 290,1160" fill="var(--yellow-mid)"/>
    <polygon class="hex label-hex" points="190,1036 217.7,1052 217.7,1084 190,1100 162.3,1084 162.3,1052" fill="var(--white)"/>
    <polygon class="hex label-hex" points="272,1061 299.7,1077 299.7,1109 272,1125 244.3,1109 244.3,1077" fill="var(--white)"/>
    <polygon class="hex label-hex" points="354,1036 381.7,1052 381.7,1084 354,1100 326.3,1084 326.3,1052" fill="var(--white)"/>
    <g class="arrows" stroke="var(--ink)" stroke-width="1.2" fill="none">
      <path d="M222,1062 H240 M236,1059 L240,1062 L236,1065"/>
      <path d="M240,1070 H222 M226,1067 L222,1070 L226,1073"/>
      <path d="M304,1062 H322 M318,1059 L322,1062 L318,1065"/>
      <path d="M322,1070 H304 M308,1067 L304,1070 L308,1073"/>
      <path d="M190,1100 V1110 H158"/>
      <path d="M272,1125 V1129"/>
      <path d="M354,1100 V1110 H388"/>
    </g>
  </svg>

  <div class="contact">
    <p>www.kestrelapiarynz.com</p>
    <p>kestrelapiarynz@postvale.com</p>
  </div>
  <div class="brand">
    <span class="brand-dot"></span>
    <span class="brand-name">Kestrel Apiary NZ Limited</span>
  </div>

  <div class="hex-text components-title" style="left:76px; top:440px; width:120px; height:120px;">
    There are 2 main components of Manuka honey which give it many health benefits:
  </div>
  <div class="hex-text component" style="left:24px; top:562px; width:108px; height:100px;">
    <span class="component-name">Hydrogen peroxide</span>
    <span class="component-desc">A powerful antibiotic compound found in large quantities in Manuka honey</span>
  </div>
  <div class="hex-text component" style="left:138px; top:562px; width:108px; height:100px;">
    <span class="component-name">Methylglyoxal</span>
    <span class="component-desc">A naturally antibiotic found in Manuka honey</span>
  </div>

  <div class="hex-text benefit" style="left:33px; top:730px; width:110px; height:112px;">
    <span>Proven health benefits of active Manuka are aiding in the treatment of:</span>
  </div>
  <div class="hex-text benefit" style="left:145px; top:730px; width:110px; height:112px;">
    <span>Burns</span><span>Fungal infections</span><span>Sore throats</span>
  </div>
  <div class="hex-text benefit" style="left:257px; top:730px; width:110px; height:112px;">
    <span>Common cold and flu</span><span>Ulcers</span><span>Cuts and abrasions</span>
  </div>
  <div class="hex-text benefit" style="left:369px; top:730px; width:110px; height:112px;">
    <span>Strengthening the immune system</span><span>Hair loss and scalp problems</span>
  </div>

  <h2 class="ratings-title">Rating<br>Equivalencies</h2>
  <div class="rating-col krf"><p>05</p><p>10</p><p>15</p><p>20</p></div>
  <div class="rating-col mgo"><p>100</p><p>250</p><p>500</p><p>800</p></div>
  <div class="rating-col npa"><p>05</p><p>10</p><p>15</p><p>20</p></div>
  <div class="scale-label krf">KRF</div>
  <div class="scale-label mgo">MGO</div>
  <div class="scale-label npa">NPA</div>

  <p class="note krf-note">KRF reveals the Non-Peroxide Activity component of Manuka Honey. It measures the strength the same way as NPA does.</p>
  <p class="note mgo-note">The MGO indicates the amount of Methylglyoxal in the honey. The higher the MGO rating the more antibacterial properties are in the honey.</p>
  <p class="note npa-note">The NPA indicates the potency of the enzymes within the Manuka Honey and its antibacterial strength.</p>
</main>
</body>
</html>
```